New Modern Design Responsive Website For Mining Company

Hi there, we need a new custom designed website for an Australian Mining company that has just relaunched.

We have just completed a new logo design contest so that will be included for you to look at.

There is an existing site to look at https://www.velbrostone.com/

Nothing should be assumed by this site other than that is the content we will be adding to it plus a blog as well. The current design and look is not at all what they want and hence why it should not be used as a base start for any new design.

They want a modern looking mobile friendly responsive design included website that appeals to the corporate market and stock investors.

They don't have a preference to colours used however colours that are considered more prestige / corporate / established and modern will most likely appeal. Colours like black/white, dark blue, gold , platinum etc would I think be more suitable but that is entirely up to you as they have not specified any colours at all.

The design should include mobile / tablet layout / design files.

If you have any questions, please get in touch any time. Thank you

Derek
Updates

Hi crew, Please confirm if you will included files for the mobile design as there has not been any mock ups from anyone showing the mobile version and how it would look? Thanks Derek

```html
<!DOCTYPE html>
<html lang="en">
<head>
<meta charset="utf-8">
<title>Gunnawarra | Velbro Stone</title>
<link href="https://fonts.googleapis.com/css2?family=Figtree:wght@400;500;600;700&display=swap" rel="stylesheet">
<style>
:root{
  --bg:#1c1c1c;
  --bg-deep:#141414;
  --text:#ffffff;
  --muted:#d2d2d2;
  --accent:#ece33b;
  --line:#6a6a6a;
}
*{box-sizing:border-box;margin:0;padding:0}
html,body{width:1200px;height:3189px;overflow:hidden}
body{background:var(--bg);color:var(--text);font-family:"Figtree",sans-serif;position:relative}
.hero-bg{position:absolute;left:0;top:0;width:1200px;height:760px;background:linear-gradient(180deg,#3a3a3a 0%,#4a4a4a 22%,#2e2e2e 55%,var(--bg) 100%)}
.footer-bg{position:absolute;left:0;top:2460px;width:1200px;height:680px;background:linear-gradient(180deg,var(--bg) 0%,#2a2a2a 45%,#222 100%)}
.info-bar{position:absolute;left:84px;width:1037px;display:flex;align-items:center;font-size:13.5px;color:var(--muted);letter-spacing:.2px}
.info-bar .item{display:flex;align-items:center;gap:6px;margin-right:36px}
.info-bar .call{margin-left:auto;color:var(--accent);font-weight:600}
.top-info{top:14px}
.top-rule{position:absolute;left:84px;top:47px;width:1037px;height:1px;background:var(--line)}
.logo{position:absolute;font-size:25px;font-weight:600;letter-spacing:1px;color:var(--text)}
.nav{position:absolute;top:66px;left:84px;width:1037px;height:40px;display:flex;align-items:center}
.nav .logo{position:static}
.nav ul{list-style:none;display:flex;gap:36px;margin-left:58px;font-size:15px;font-weight:500}
.nav .cta{margin-left:auto;background:var(--accent);color:#111;font-weight:600;font-size:15px;padding:10px 21px}
.page-title{position:absolute;top:195px;left:0;width:1200px;text-align:center;font-size:50px;font-weight:600}
.copy{position:absolute;left:84px;width:1037px;font-size:15.3px;line-height:25px;color:#e8e8e8}
.copy p+p{margin-top:25px}
.photo{position:absolute;border-radius:2px}
.photo-main{left:82px;top:789px;width:1036px;height:489px;background:linear-gradient(180deg,#7ea6d6 0%,#b7c6d4 20%,#9a8570 35%,#b48c5e 65%,#8e6a44 100%)}
.photo-a{left:82px;top:2123px;width:314px;height:247px;background:linear-gradient(180deg,#8fa3b5 0%,#6a5f52 35%,#a36a45 100%)}
.photo-b{left:441px;top:2123px;width:314px;height:247px;background:linear-gradient(180deg,#9eb3c6 0%,#a89b86 35%,#c6b39b 100%)}
.photo-c{left:804px;top:2123px;width:314px;height:247px;background:linear-gradient(160deg,#9b8469 0%,#c7a47a 50%,#7b5f44 100%)}
.samples{position:absolute;left:82px;top:1638px;list-style:none;font-size:15.3px;color:#e8e8e8}
.samples li{height:50px}
.cta-title{position:absolute;left:84px;top:2550px;font-size:40px;font-weight:600}
.field{position:absolute;top:2635px;width:320px;border-bottom:1px solid var(--line);padding-bottom:14px;font-size:14px;color:var(--muted)}
.btn{position:absolute;left:84px;top:2715px;width:211px;height:40px;border:1.5px solid var(--accent);display:flex;align-items:center;justify-content:center;gap:10px;font-size:15.5px;color:var(--text)}
.footer-rule{position:absolute;left:84px;top:2811px;width:1037px;height:1px;background:var(--line)}
.footer-logo{left:84px;top:2862px}
.footer-col{position:absolute;top:2866px}
.footer-col h4{font-size:15.5px;font-weight:600;color:var(--accent);margin-bottom:18px}
.footer-col li{list-style:none;font-size:15.5px;color:#cfcfcf;height:33px}
.bottom-info{top:3097px}
.copyright{position:absolute;left:0;top:3139px;width:1200px;height:50px;background:var(--bg-deep);display:flex;align-items:center;justify-content:center;font-size:15px;color:#a8a8a8}
</style>
</head>
<body>
<div class="hero-bg" role="img" aria-label="Greyscale photograph of a mining haul truck at a quarry"></div>

<div class="info-bar top-info">
  <span class="item"><svg width="10" height="13" viewBox="0 0 10 13"><path d="M5 12S1 7.5 1 5a4 4 0 0 1 8 0c0 2.5-4 7-4 7z" fill="none" stroke="#ece33b" stroke-width="1.2"/><circle cx="5" cy="5" r="1.4" fill="#ece33b"/></svg>SUITE 4.12B, LEVEL 4, HARBOURVIEW TOWER, 88 KENT LANE, SYDNEY NSW 2000</span>
  <span class="item"><svg width="12" height="12" viewBox="0 0 12 12"><circle cx="6" cy="6" r="5" fill="none" stroke="#ece33b" stroke-width="1.2"/><path d="M6 3v3l2 1.5" fill="none" stroke="#ece33b" stroke-width="1.2"/></svg>MON - FRI 8AM - 5PM</span>
  <span class="call">Call for a free estimate • 555 210 4870</span>
</div>
<div class="top-rule"></div>

<nav class="nav">
  <span class="logo">VELBRO STONE</span>
  <ul><li>CORPORATE</li><li>GOVERNANCE</li><li>INVESTORS</li><li>PORTFOLIO ▾</li><li>ANNUAL REPORTS</li></ul>
  <span class="cta">CONTACT</span>
</nav>

<h1 class="page-title">Gunnawarra</h1>

<div class="copy" style="top:354px">
  <p>roject area is approximately 130km south-south-west of Cairns, 108km south-south-west of Mareeba and 214km north-west of Townsville, an approved Cobalt and Nickel export port. &nbsp; Access is readily available via the Kennedy Highway from Mareeba and thence via the Gunnawarra Road, a formed and graded council road. &nbsp;Gunnawarra Station has a rural airfield. &nbsp;Several tracks dissect the project area giving good vehicle access to most of the tenement. &nbsp;The project lies adjacent to and overlays tenements associated with Southland Minerals Limited Tarrow Cobalt-Nickel-Scandium project.</p>
  <p>The climate of the area is sub-tropical, being warm and dry in winter and hot and wet in summer. &nbsp;Two thirds of the rainfall occurs between December and March. &nbsp;The mean annual rainfall recorded at Mt Garnet is 781mm. &nbsp;The average maximum daily temperature ranges from 21ºC to 35ºC. Vegetation across the Gunnawarra project areas is mapped as predominantly Category B Remnant vegetation with some areas of Category X Vegetation. &nbsp;Approximately 50% of the vegetation on site at EPM 26560 consists of RE 9.5.5a/9.5.6a considered least concern under the Vegetation Management Act, the remainder being a mix of Res 9.11.26a, 9.5.8, 9.8.4, 9.8.1 and 9.3.10a. Open woodland that is both sparse and mid-dense consisting of Corymbia clarksoniana, Eucalyptus leptophleba, Eucalyptus portuensis, E.cebra and Corymbia citriodora. &nbsp;At EPM 26599 the dominant vegetation consists of RE 9.11.5, sparse woodland of Eucalyptus persistens, and E. crebra with a sub canopy of Carissa lanceolata and Acacia spp. &nbsp;Themeda triandra (kangaroo grass) and Heteropogon triticeus (giant spear grass) are the main grass species.</p>
</div>

<div class="photo photo-main" role="img" aria-label="Photograph of an excavator and haul trucks working an open-cut mine under a blue sky"></div>

<div class="copy" style="top:1337px;left:82px">
  <p>The topography is generally gently undulating sitting between the 720m and 620m contours and forms part of a Tertiary laterite land surface. &nbsp;The land surface is in an advanced state of dissection with the laterite capping having been partially stripped off, revealing scattered low hills and small ranges of pre-tertiary rocks. &nbsp;The area contains a variety of physiographic features including hills, small ranges, mesas, plateaus and valleys.</p>
  <p>The Gunnawarra Project consists of EPM 26560 located 30km south of Mt Garnet in Far North Queensland and EPM 26599, 17 km south of Greenvale both of which are held by Corvane Holdings Pty Ltd. &nbsp;EPM 26560 was granted on 24th November 2017 for a period of two years and a renewal has been lodged; EPM 26599 was granted on 24th November 2018 also for a period of two years. &nbsp;Since grant, exploration work has concentrated on EPM 26560 and has comprised of site visits, localised sampling (returning anomalous Platinum and Palladium confirming the potential Sulphide extension), assay work and desk top research, table 1.</p>
</div>

<ul class="samples">
  <li>CORVANE EPM 26560 Gunnawarra (GW)</li>
  <li>Surface Sample highlights (July 2018) include;</li>
  <li>GW105 - Cobalt - 4430ppm</li>
  <li>GW101 - Nickel - 14,350ppm</li>
  <li>GW87 - Copper - 2320ppm</li>
  <li>GW87 - Scandium - 60ppm</li>
  <li>GW107 - Chromite - 13,500ppm</li>
  <li>GW105 - Manganese - 228,000ppm</li>
  <li>Table 1. Surface Sample Highlights EPM 26560</li>
</ul>

<div class="photo photo-a" role="img" aria-label="Photograph of a haul truck on terraced open-pit benches"></div>
<div class="photo photo-b" role="img" aria-label="Photograph of a mineral processing plant with conveyors"></div>
<div class="photo photo-c" role="img" aria-label="Photograph of a dragline working over spoil heaps"></div>

<div class="footer-bg" role="img" aria-label="Faint greyscale photograph of mining machinery"></div>

<h2 class="cta-title">Ready to work with us?</h2>
<div class="field" style="left:84px">Full Name</div>
<div class="field" style="left:440px">Email Address</div>
<div class="field" style="left:801px">Contact Number</div>
<div class="btn">REQUEST A QUOTE <svg width="18" height="10" viewBox="0 0 18 10"><path d="M0 5h16M12 1l4 4-4 4" fill="none" stroke="#ece33b" stroke-width="1.5"/></svg></div>

<div class="footer-rule"></div>
<span class="logo footer-logo">VELBRO STONE</span>
<div class="footer-col" style="left:293px"><h4>CORPORATE</h4><ul><li>Our Team</li><li>About Us</li></ul></div>
<div class="footer-col" style="left:454px"><h4>GOVERNANCE</h4><ul><li>Notices</li><li>Text</li><li>Text</li></ul></div>
<div class="footer-col" style="left:630px"><h4>INVESTORS</h4><ul><li>Investors</li><li>Meeting Notices</li><li>Others</li></ul></div>
<div class="footer-col" style="left:818px"><h4>PORTFOLIO</h4><ul><li>Gunnawarra</li><li>Mt. Jesse</li><li>Pluton</li></ul></div>
<div class="footer-col" style="left:976px"><h4>ANNUAL REPORTS</h4><ul><li>Latest Reports</li><li>Report Archive</li><li>Text</li></ul></div>

<div class="info-bar bottom-info" style="left:81px">
  <span class="item"><svg width="10" height="13" viewBox="0 0 10 13"><path d="M5 12S1 7.5 1 5a4 4 0 0 1 8 0c0 2.5-4 7-4 7z" fill="none" stroke="#ece33b" stroke-width="1.2"/><circle cx="5" cy="5" r="1.4" fill="#ece33b"/></svg>SUITE 4.12B, LEVEL 4, HARBOURVIEW TOWER, 88 KENT LANE, SYDNEY NSW 2000</span>
  <span class="item"><svg width="12" height="12" viewBox="0 0 12 12"><circle cx="6" cy="6" r="5" fill="none" stroke="#ece33b" stroke-width="1.2"/><path d="M6 3v3l2 1.5" fill="none" stroke="#ece33b" stroke-width="1.2"/></svg>MON - FRI 8AM - 5PM</span>
  <span class="call">Call for a free estimate • 555 210 4870</span>
</div>

<footer class="copyright">Copyright © 2022 Velbrostone LTD</footer>
</body>
</html>
```